Internet Flyer for Voip and Fast Internet

I need a 2 sided A5 flyer for a bespoke service to residential flats...

Needs to stand out after dropping through the door...!

Target Market(s)

Central City Flats - High value occupants.

Industry/Entity Type

Residential

```html
<!DOCTYPE html>
<html lang="en">
<head>
<meta charset="utf-8">
<title>Northlane Telecom – Four Play Flyer</title>
<link href="https://fonts.googleapis.com/css2?family=Source+Sans+3:wght@400;600;700&display=swap" rel="stylesheet">
<style>
  :root {
    --page-bg: #000000;
    --canvas-bg: #ffffff;
    --green: #8cc63f;
    --green-dark: #2f9a3a;
    --green-light: #c9e6a8;
    --text: #ffffff;
  }
  * { margin: 0; padding: 0; box-sizing: border-box; }
  html, body {
    width: 1200px; height: 830px; overflow: hidden;
    background: var(--canvas-bg);
    font-family: "Source Sans 3", "Myriad Pro", Arial, sans-serif;
  }
  .canvas { position: relative; width: 1200px; height: 830px; }
  .page {
    position: absolute; top: 15px; width: 542px; height: 767px;
    background: var(--page-bg); color: var(--text); overflow: hidden;
  }
  .page--front { left: 25px; }
  .page--back { left: 598px; }
  .tile-strip {
    position: absolute; left: 0; top: 0; width: 56px; height: 100%;
  }
  .headline { position: absolute; color: var(--green); font-weight: 400; line-height: 1; white-space: nowrap; }
  .headline small { font-size: 24px; }
  .headline--making { left: 102px; top: 32px; font-size: 34px; }
  .headline--better { left: 132px; top: 80px; font-size: 42px; }
  .headline--invest { left: 257px; top: 118px; font-size: 42px; }
  .offer-box {
    position: absolute; left: 72px; top: 175px; width: 452px; height: 163px;
    border: 5px solid var(--green); border-radius: 18px; color: var(--green);
  }
  .offer-question {
    position: absolute; left: 14px; top: 14px; width: 200px;
    text-align: center; line-height: 1; font-size: 30px;
  }
  .offer-question .tiny { font-size: 12px; }
  .offer-question .mid { font-size: 22px; }
  .offer-cta { position: absolute; right: 10px; top: 34px; text-align: center; }
  .offer-cta__lead { font-size: 24px; margin-right: 60px; }
  .offer-cta__name { font-size: 44px; font-weight: 700; line-height: 1.2; }
  .packages {
    position: absolute; left: 77px; top: 357px; width: 460px;
    font-size: 13px; line-height: 15.5px;
  }
  .package { margin-bottom: 9px; }
  .package__title { color: var(--green); }
  .package__title span { margin-left: 24px; }
  .package__list { padding-left: 122px; list-style: none; }
  .package__list--spaced { margin-top: 14px; }
  .pitch { margin-top: 4px; width: 430px; }
  .signature {
    position: absolute; left: 279px; top: 723px; color: var(--green); font-size: 20px;
  }
  .benefits { position: absolute; left: 80px; top: 56px; width: 428px; }
  .benefits h2 { color: var(--green); font-size: 22px; font-weight: 700; margin-bottom: 14px; }
  .benefits ul { list-style: none; }
  .benefits li {
    font-size: 13px; line-height: 17.4px; text-align: justify; margin-bottom: 10px;
  }
  .benefits li::before {
    content: ""; display: inline-block; width: 11px; height: 11px;
    background: var(--green); margin-right: 5px; vertical-align: -1px;
  }
</style>
</head>
<body>
<div class="canvas">
  <section class="page page--front">
    <svg class="tile-strip" role="img" aria-label="Decorative column of green tiles" viewBox="0 0 56 767" preserveAspectRatio="none">
      <defs>
        <linearGradient id="stripFront" x1="0" y1="0" x2="1" y2="1">
          <stop offset="0" stop-color="#3fae49"/>
          <stop offset="0.5" stop-color="#7cc36b"/>
          <stop offset="1" stop-color="#2f9a3a"/>
        </linearGradient>
      </defs>
      <rect width="56" height="767" fill="url(#stripFront)"/>
    </svg>

    <h1 class="headline headline--making">Making <small>an</small></h1>
    <div class="headline headline--better">even better</div>
    <div class="headline headline--invest">investment!</div>

    <div class="offer-box">
      <p class="offer-question">
        <span class="mid">fed up</span> <span class="tiny">with</span><br>
        slow internet<br>
        <span class="tiny">and</span> expensive<br>
        phone calls?
      </p>
      <div class="offer-cta">
        <p class="offer-cta__lead">Try our</p>
        <p class="offer-cta__name">‘Four Play’</p>
      </div>
    </div>

    <div class="packages">
      <div class="package">
        <p class="package__title">Phone Package - <span>Available now</span></p>
        <ul class="package__list">
          <li>Line Rental only £4.99 per month</li>
          <li>Cheap Calls to the world – eg USA – 1p per min, China 2p per min</li>
          <li>Free Calls to the same network</li>
        </ul>
      </div>
      <div class="package">
        <p class="package__title">Internet Packages – Sign Up Now</p>
        <ul class="package__list">
          <li>100Mbs up and down - £249 install and £99.00 per month</li>
          <li>Faster Speeds are Available – up to 1 Gbs</li>
        </ul>
      </div>
      <div class="package">
        <p class="package__title">TV and HiFi over the Internet – Tell us what services you need</p>
        <ul class="package__list package__list--spaced">
          <li>Aurelo – Tunebay, Melodix etc</li>
          <li>Lumitek</li>
          <li>iPTV</li>
          <li>etc etc..</li>
        </ul>
      </div>
      <div class="package">
        <p class="package__title">Corvan Telepresence – contact us for further information!</p>
      </div>
      <p class="pitch">Remember the TV Program Zero Hour? Do you need to connect with people? We are able to connect you to the video world to give you High Definition 50”+ Video Calls and Conferencing.....</p>
    </div>

    <p class="signature">Northlane Telecom Group Ltd</p>
  </section>

  <section class="page page--back">
    <svg class="tile-strip" role="img" aria-label="Decorative column of green tiles" viewBox="0 0 56 767" preserveAspectRatio="none">
      <defs>
        <linearGradient id="stripBack" x1="0" y1="0" x2="1" y2="1">
          <stop offset="0" stop-color="#3fae49"/>
          <stop offset="0.5" stop-color="#7cc36b"/>
          <stop offset="1" stop-color="#2f9a3a"/>
        </linearGradient>
      </defs>
      <rect width="56" height="767" fill="url(#stripBack)"/>
    </svg>

    <div class="benefits">
      <h2>Benefits of Bandwidth</h2>
      <ul>
        <li>Delay kills all forms of human interaction and creativity. Less delay results in more effective interaction, innovation and output, and the relationship is highly non-linear so less delay translates into far more output.</li>
        <li>Ubiquitous (and symmetrical) videoconferencing that actually works can dramatically reduce our need to travel.</li>
        <li>Real-time (multi-user) collaborative environments can further accelerate (global) creativity and productivity by making virtual teaming a working reality.</li>
        <li>Imagine instantaneous access to information sources and resources of all kinds of forms and formats - uploads and downloads.</li>
        <li>Cloud computing with all applications and data online would dramatically reduce hardware and software costs, improve security markedly, and spawn new communities, business opportunities and industries.</li>
        <li>Virtual and augmented reality would come alive and change absolutely everything from working to entertainment, education, training and healthcare - and we can't even hazard a guess at the scale of improvement to be had.</li>
        <li>All forms of modelling and prediction - scientific, industrial, social and so on would be revolutionised by instant access to distributed resources worldwide.</li>
        <li>3D prototyping and distributed production would become real and a part of the mainstream, and ultimately the new mainstream industry.</li>
        <li>Real-time access to global radio, TV, movies and other forms of entertainment at our convenience.</li>
        <li>Vast tracts of radio spectrum for high-speed wireless apps would become available as services delivered by 'by fibre' reduce the need for services 'by radio'</li>
      </ul>
    </div>
  </section>
</div>
</body>
</html>
```